Brantwell Group needs a business card design

We need a new business card design using the logo recently selected in a logo competition on Pixel Forum. Our business is a consultancy specializing in aviation and energy and the winning business card design will promote an image of precision and professionalism with creativity.

Please use the logo with the name on the front of the card and use a complementary font. Make the back white with either the light grey or dark grey logo.

Target Market(s)

Senior finance and legal leaders at aviation and energy companies

Industry/Entity Type

Management Consulting

Contact Information for Business Card

Peter Haldane
President
Brantwell Group

www.brantwellgroup.example

(555) 304-6198
ph@brantwellgroup.example

Requirements
Must have
• Professional font that goes well with the logo font

```html
<!DOCTYPE html>
<html lang="en">
<head>
<meta charset="utf-8">
<title>Brantwell Group – Business Card</title>
<link href="https://fonts.googleapis.com/css2?family=Questrial&display=swap" rel="stylesheet">
<style>
  :root {
    --navy: #0f3f6e;
    --ink: #2b2b2b;
    --card-white: #ffffff;
    --rule: #b9b9b9;
    --mist: #e4e5e7;
    --backdrop: #1c1c1c;
  }
  * { margin: 0; padding: 0; box-sizing: border-box; }
  html, body {
    width: 1200px; height: 1200px; overflow: hidden;
    background: var(--backdrop);
    font-family: "Questrial", "Helvetica Neue", Arial, sans-serif;
  }
  .canvas { position: relative; width: 1200px; height: 1200px; }
  .card {
    position: absolute; left: 301px; width: 598px; height: 364px; overflow: hidden;
  }
  .card-front { top: 230px; background: var(--card-white); }
  .card-back { top: 622px; background: var(--navy); }

  .corner-band { position: absolute; left: 0; top: 0; }

  .brand-lockup {
    position: absolute; left: 0; width: 292px; top: 240px;
    display: flex; align-items: center; justify-content: center; gap: 9px;
    color: var(--navy); font-size: 22px; letter-spacing: 0.5px; white-space: nowrap;
  }
  .brand-dot { width: 10px; height: 10px; background: var(--navy); }

  .divider {
    position: absolute; left: 341px; top: 152px; width: 1px; height: 172px;
    background: var(--rule); transform: translateX(-49px);
  }

  .person { position: absolute; left: 343px; top: 66px; color: var(--ink); }
  .person-name { font-size: 22px; line-height: 1.1; }
  .person-title { font-size: 15px; margin-top: 4px; }

  .contact-row {
    position: absolute; left: 318px; display: flex; align-items: flex-start; gap: 8px;
    color: var(--ink); font-size: 14.5px; line-height: 16px; white-space: nowrap;
  }
  .contact-row svg { flex: none; width: 15px; height: 15px; fill: var(--navy); margin-top: 1px; }
  .contact-address { top: 163px; }
  .contact-phone { top: 234px; }
  .contact-email { top: 263px; }
  .contact-web { top: 293px; }

  .back-brand {
    position: absolute; left: 0; right: 0; top: 132px;
    display: flex; align-items: center; justify-content: center; gap: 16px;
    color: var(--mist); font-size: 46px; letter-spacing: 1px; white-space: nowrap;
  }
  .back-brand-dot { width: 20px; height: 20px; background: var(--mist); }
  .back-url {
    position: absolute; left: 87px; top: 292px;
    color: var(--mist); font-size: 16.5px;
  }
</style>
</head>
<body>
<main class="canvas">
  <section class="card card-front">
    <svg class="corner-band" width="120" height="164" viewBox="0 0 120 164" aria-hidden="true">
      <polygon points="0,70 92,0 119,0 0,163" fill="var(--navy)"/>
    </svg>

    <div class="brand-lockup"><span class="brand-dot"></span>Brantwell Group</div>

    <div class="divider"></div>

    <div class="person">
      <p class="person-name">Peter Haldane</p>
      <p class="person-title">President</p>
    </div>

    <div class="contact-row contact-address">
      <svg viewBox="0 0 24 24" aria-hidden="true"><path d="M12 2a7 7 0 0 0-7 7c0 5 7 13 7 13s7-8 7-13a7 7 0 0 0-7-7zm0 9.5A2.5 2.5 0 1 1 12 6.5a2.5 2.5 0 0 1 0 5z"/></svg>
      <p>Address will go here<br>Unit 12, Harbour Row, Eastfield<br>Addt. information on location</p>
    </div>
    <div class="contact-row contact-phone">
      <svg viewBox="0 0 24 24" aria-hidden="true"><path d="M12 2a10 10 0 0 0-8.6 15.1L2 22l5-1.3A10 10 0 1 0 12 2zm0 2a8 8 0 1 1-4.1 14.9l-.3-.2-2.8.7.8-2.7-.2-.3A8 8 0 0 1 12 4zm-3 3.5c-.3 0-.7.1-1 .5-.3.4-1 1-1 2.4s1 2.8 1.2 3c.1.2 2 3.2 5 4.3 2.4.9 2.9.8 3.5.7.5-.1 1.7-.7 1.9-1.4.2-.7.2-1.2.2-1.4l-.5-.3-1.9-.9c-.3-.1-.5-.1-.7.2l-.8 1c-.2.2-.3.2-.6.1a6.6 6.6 0 0 1-3.3-2.9c-.2-.4.3-.4.8-1.3.1-.2 0-.4 0-.5l-.9-2.1c-.2-.5-.4-.4-.6-.4z"/></svg>
      <p>(555) 304-6198</p>
    </div>
    <div class="contact-row contact-email">
      <svg viewBox="0 0 24 24" aria-hidden="true"><path d="M2 6h20v12H2z M3 6.5l9 7 9-7" /></svg>
      <p>ph@brantwellgroup.example</p>
    </div>
    <div class="contact-row contact-web">
      <svg viewBox="0 0 24 24" aria-hidden="true"><circle cx="5" cy="19" r="2.2"/><path d="M3 10a11 11 0 0 1 11 11h-2.5A8.5 8.5 0 0 0 3 12.5zM3 4a17 17 0 0 1 17 17h-2.5A14.5 14.5 0 0 0 3 6.5z"/></svg>
      <p>www.brantwellgroup.example</p>
    </div>
  </section>

  <section class="card card-back">
    <div class="back-brand"><span class="back-brand-dot"></span>Brantwell Group</div>
    <p class="back-url">www.brantwellgroup.example</p>
  </section>
</main>
</body>
</html>
```